Global Aviation Services website

we are a start up airline/aviation services company that will operate in Australia, USA and New Zealand initially. Fundamentally the service is to airlines who fly into and out of a market yet do not wish to have their own admin, sales and marketing infrastructures. They would use us.
The company name is Veltaro.
It needs to look sophisticated, sharp and professional. We would like it designed and built in the CMS - wordpress so we can update after the project is finished when necessary. An example of who we are and a good website we like can be found at: http://pembrikegroup.example/. There is no ecommerce or interactivity other than a contact us. We do like animation for promotion. There will be links to our airline clients and sub sites or pages will exist for the various offices we have globally. Currently 6. Each of these offices will have a dedicated local URL. Please submit your suggestion of a home page and 2 internal pages. Thank you and kind regards Miriam
Target Market(s)
airlines, airline technology companies,
Industry/Entity Type
Aviation
Coding
Coded - Design and coding required
Number of Pages Required
5+ page
Look and feel

```html
<!DOCTYPE html>
<html lang="en">
<head>
<meta charset="utf-8">
<title>Veltaro — Global Aviation Services</title>
<link href="https://fonts.googleapis.com/css2?family=Roboto+Condensed:wght@400;700&family=Roboto+Slab:wght@400;700&family=Roboto:wght@400;700&display=swap" rel="stylesheet">
<style>
:root{
  --purple:#6a3f9c;
  --purple-dark:#3b2a6b;
  --red:#e02a2a;
  --ink:#333;
  --grey-bg:#eeeeee;
  --white:#fff;
}
*{box-sizing:border-box;margin:0;padding:0}
html,body{width:704px;height:1200px;overflow:hidden;background:#fff}
body{position:relative;font-family:Arial,Helvetica,sans-serif;color:var(--ink)}
.abs{position:absolute}
.topbar{left:0;top:0;width:704px;height:20px;background:var(--purple);color:#fff;font:8.5px 'Roboto Slab',serif;text-align:center;line-height:18px;border-bottom:2px solid #fff}
.header{left:0;top:20px;width:704px;height:62px;background:#fff}
.brand{left:50px;top:4px;font:700 36px 'Roboto Condensed',sans-serif;color:var(--purple-dark);letter-spacing:1px}
.phone{right:56px;top:9px;font:12px Roboto,sans-serif;color:#333;display:flex;align-items:center;gap:5px}
.nav{right:60px;top:43px;display:flex;font:9.5px 'Roboto Slab',serif;color:#333}
.nav a{color:inherit;text-decoration:none;padding:0 12px;border-left:1px solid #999;line-height:11px}
.nav a:first-child{border:0;color:var(--purple);font-weight:700}
.hero{left:0;top:82px;width:704px;height:263px;background:linear-gradient(90deg,#eef0f2 0%,#e4e7ea 45%,#cfd6de 70%,#9fb0c4 100%)}
.hero-title{left:50px;top:72px;width:230px;font:400 16.5px/25px 'Roboto Condensed',sans-serif;color:#333}
.arrow{width:22px;height:20px;background:#333;display:flex;align-items:center;justify-content:center}
.section-title{width:704px;text-align:center;font:400 15.5px 'Roboto Slab',serif;color:var(--purple)}
.rule{left:120px;width:464px;height:1px;background:#ccc}
.rule::after{content:"";position:absolute;left:192px;top:-1px;width:80px;height:2px;background:var(--red)}
.welcome-text{left:60px;top:402px;width:584px;font:8px/13px Arial,sans-serif;text-align:center;color:#333}
.readmore{left:0;width:704px;top:460px;text-align:center;font:7px Arial,sans-serif;color:var(--purple);text-decoration:underline}
.services{left:0;top:494px;width:704px;height:284px;background:var(--grey-bg)}
.card{top:61px;width:144px;height:182px;background:#fff;border:1px solid #ccc}
.card h3{height:22px;background:var(--purple);color:#fff;font:400 9.5px/22px 'Roboto Condensed',sans-serif;padding-left:5px}
.card .photo{margin:3px 3px 0;height:84px}
.card p{font:7.2px/11.5px Arial,sans-serif;padding:7px 5px;color:#333}
.plus{left:64px;bottom:-9px;width:16px;height:16px;border-radius:50%;background:var(--purple);color:#fff;font:bold 11px/16px Arial;text-align:center}
.client{top:842px;width:98px;height:52px;background:#ececec;display:flex;align-items:center;justify-content:center;gap:6px;font:700 11px/11px 'Roboto Condensed',sans-serif;color:#c8c8c8}
.client i{width:14px;height:14px;background:#d2d2d2;border-radius:50%;display:block}
.chev{top:856px;font:20px Arial;color:#888}
.cta{left:0;top:917px;width:704px;height:53px;background:var(--purple)}
.cta p{position:absolute;left:57px;top:9px;width:440px;font:700 13px/19px 'Roboto Condensed',sans-serif;color:#fff}
.cta-btn{left:504px;top:7px;width:134px;height:40px;background:var(--red);color:#fff;text-align:center;border-radius:2px}
.cta-btn small{display:block;font:10px/12px Arial;padding-top:4px}
.cta-btn strong{display:block;font:400 16px/20px Arial}
.footer{left:0;top:970px;width:704px;height:208px;background:linear-gradient(135deg,#3d3d3d,#2f2f2f)}
.contact h4{font:400 13px 'Roboto Slab',serif;color:#fff;position:absolute;left:51px;top:10px}
.contact .line{left:51px;top:30px;width:185px;height:1px;background:#777}
.contact .line::after{content:"";position:absolute;left:0;top:-1px;width:48px;height:2px;background:var(--red)}
.citem{left:57px;display:flex;gap:10px;font:8.4px/12px Arial,sans-serif;color:#fff}
.citem svg{flex:none;width:12px;height:12px;margin-top:1px}
.footer-brand{left:272px;top:82px;font:700 40px 'Roboto Condensed',sans-serif;color:#fff;letter-spacing:2px}
.inquiry{left:453px;top:10px;width:184px;height:193px;background:rgba(90,90,90,.85);border-top:2px solid var(--purple)}
.inquiry h4{position:absolute;left:40px;top:12px;font:400 12px 'Roboto Slab',serif;color:#fff}
.inquiry .icon{left:9px;top:9px;width:24px;height:24px;border-radius:50%;background:#fff;display:flex;align-items:center;justify-content:center}
.inquiry .lead{left:9px;top:46px;font:7.5px Arial;color:#fff}
.field{left:8px;width:168px;height:19px;background:rgba(140,140,140,.6);font:7.5px/19px Arial;color:#ddd;padding-left:7px}
.submit{left:8px;top:167px;width:70px;height:19px;background:var(--red);color:#fff;font:700 10px/19px Arial;text-align:center}
.bottombar{left:0;top:1178px;width:704px;height:22px;background:var(--purple);color:#fff;font:7.5px/22px Arial;text-align:center}
</style>
</head>
<body>
<div class="abs topbar">We Are A Airline / Aviation Services Company That Will Operate In Australia, USA And New Zealand</div>

<header class="abs header">
  <div class="abs brand">Veltaro</div>
  <div class="abs phone">
    <svg width="16" height="16" viewBox="0 0 16 16"><circle cx="8" cy="8" r="7" fill="none" stroke="#e02a2a" stroke-width="1.3"/><path d="M6 4.5l1.2 2-1 1a5 5 0 0 0 2.3 2.3l1-1 2 1.2-.8 1.4c-3 0-5.9-2.9-5.9-5.9z" fill="#e02a2a"/></svg>
    123-555-0187
  </div>
  <nav class="abs nav"><a>Home</a><a>About Us</a><a>Our Services</a><a>FAQ's</a><a>Contact Us</a></nav>
</header>

<section class="abs hero" role="img" aria-label="Smiling businessman at a laptop in a bright office">
  <h1 class="abs hero-title">We Provide Service Is To Airlines Who Fly Into And Out Of A Market Yet Do Not Wish To Have Their Own Admin, Sales And Marketing Infrastructures.</h1>
  <div class="abs arrow" style="left:4px;top:122px"><svg width="8" height="10"><path d="M6 1L2 5l4 4" stroke="#fff" stroke-width="2" fill="none"/></svg></div>
  <div class="abs arrow" style="left:678px;top:106px"><svg width="8" height="10"><path d="M2 1l4 4-4 4" stroke="#fff" stroke-width="2" fill="none"/></svg></div>
</section>

<h2 class="abs section-title" style="top:362px">Welcome to <span style="font-family:'Roboto Condensed',sans-serif;font-weight:700;color:var(--purple-dark)">Veltaro</span></h2>
<div class="abs rule" style="top:392px"></div>
<p class="abs welcome-text">Lorem ipsum dolor sit amet, consectetuer adipiscing elit, sed diam nonummy nibh euismod tincidunt ut laoreet dolore magna aliquam erat volutpat. Ut wisi enim ad minim veniam, quis nostrud exerci tation ullamcorper suscipit lobortis nisl ut aliquip ex ea commodo consequat. Duis autem vel eum iriure dolor in hendrerit in vulputate velit esse molestie consequat, vel illum dolore eu feugiat nulla facilisis at vero eros et accumsan et iusto odio dignissim qui blandit praesent luptatum zzril delenit augue duis dolore te feugait nulla facilisi.Lorem ipsum dolor sit amet, consectetuer</p>
<a class="abs readmore">Read more</a>

<section class="abs services">
  <h2 class="abs section-title" style="top:18px">Our Services</h2>
  <div class="abs rule" style="top:43px"></div>
  <article class="abs card" style="left:55px"><h3>Admin Department</h3><div class="photo" role="img" aria-label="Airline staff member in an office" style="background:linear-gradient(135deg,#8aa0b8,#2c3648)"></div><p>Lorem ipsum dolor consectuer. Lorem ipsum dolor consectetuer ipsum dolor consectuer. Lorem ipsum.consectuer. Lorem ipsum.</p><div class="abs plus">+</div></article>
  <article class="abs card" style="left:205px"><h3>Sales Service</h3><div class="photo" role="img" aria-label="Hand touching a sales chart screen" style="background:linear-gradient(135deg,#555,#c9c9c9 60%,#777)"></div><p>Lorem ipsum dolor consectuer. Lorem ipsum dolor consectetuer ipsum dolor consectuer. Lorem ipsum.consectuer. Lorem ipsum.</p><div class="abs plus">+</div></article>
  <article class="abs card" style="left:354px"><h3>Marketing Infrastructures</h3><div class="photo" role="img" aria-label="Cargo aircraft on the apron at dusk" style="background:linear-gradient(180deg,#6d86b0,#c7a98a 60%,#4a4a48)"></div><p>Lorem ipsum dolor consectuer. Lorem ipsum dolor consectetuer ipsum dolor consectuer. Lorem ipsum.consectuer. Lorem ipsum.</p><div class="abs plus">+</div></article>
  <article class="abs card" style="left:504px"><h3>Ground Handling Services</h3><div class="photo" role="img" aria-label="Ground crew marshalling a jet" style="background:linear-gradient(180deg,#7fa6d6,#c9d6e4 55%,#8a8f86)"></div><p>Lorem ipsum dolor consectuer. Lorem ipsum dolor consectetuer ipsum dolor consectuer. Lorem ipsum.consectuer. Lorem ipsum.</p><div class="abs plus">+</div></article>
</section>

<h2 class="abs section-title" style="top:800px">Our Airline Clients</h2>
<div class="abs rule" style="top:825px"></div>
<div class="abs chev" style="left:33px">‹</div>
<div class="abs client" style="left:55px"><i></i>LOGO<br>BRAND</div>
<div class="abs client" style="left:179px"><i></i>LOGO<br>BRAND</div>
<div class="abs client" style="left:303px"><i></i>LOGO<br>BRAND</div>
<div class="abs client" style="left:427px"><i></i>LOGO<br>BRAND</div>
<div class="abs client" style="left:551px"><i></i>LOGO<br>BRAND</div>
<div class="abs chev" style="left:660px">›</div>

<section class="abs cta">
  <p>Lorem ipsum dolor sit amet consectetur adipisicing elitsed do eiusmod tempor incididunt ut labore dolo magna aliqua.</p>
  <div class="abs cta-btn"><small>Call Us Today</small><strong>913-555-0142</strong></div>
</section>

<footer class="abs footer" role="img" aria-label="Dark street map background">
  <div class="contact">
    <h4>Contact Details</h4>
    <div class="abs line"></div>
    <div class="abs citem" style="top:42px"><svg viewBox="0 0 12 12"><path d="M6 0a4 4 0 0 1 4 4c0 3-4 8-4 8S2 7 2 4a4 4 0 0 1 4-4z" fill="#fff"/><circle cx="6" cy="4" r="1.5" fill="#3a3a3a"/></svg><div>Postal Address<br>Street Name, City Name State Zip code</div></div>
    <div class="abs citem" style="top:75px"><svg viewBox="0 0 12 12"><path d="M2 1l2.5 0 1 3-1.5 1a6 6 0 0 0 3 3l1-1.5 3 1V11C6 11 1 6 1 1z" fill="#fff"/></svg><div>Telephone<br>123-555-0187</div></div>
    <div class="abs citem" style="top:109px"><svg viewBox="0 0 12 12"><rect x="1" y="4" width="10" height="6" fill="#fff"/><rect x="3" y="1" width="6" height="3" fill="#fff"/></svg><div>Fax<br>124-555-0163</div></div>
    <div class="abs citem" style="top:142px"><svg viewBox="0 0 12 12"><rect x="1" y="3" width="10" height="7" fill="#fff"/><path d="M1 3l5 4 5-4" stroke="#3a3a3a" fill="none"/></svg><div>Email<br>Support: inquiry@veltaro.example</div></div>
    <div class="abs citem" style="top:175px"><svg viewBox="0 0 12 12"><rect x="3" y="1" width="6" height="10" fill="#fff"/></svg><div>Facebook<br>www.facebook.com/Veltaro</div></div>
  </div>
  <div class="abs footer-brand">Veltaro</div>
  <form class="abs inquiry">
    <div class="abs icon"><svg width="12" height="12" viewBox="0 0 12 12"><path d="M2 1l2.5 0 1 3-1.5 1a6 6 0 0 0 3 3l1-1.5 3 1V11C6 11 1 6 1 1z" fill="#666"/></svg></div>
    <h4>Quick Inquiry</h4>
    <div class="abs lead">Lorem ipsum dolor sit amet, consectetuer</div>
    <div class="abs field" style="top:63px">Name</div>
    <div class="abs field" style="top:85px">Email</div>
    <div class="abs field" style="top:107px">Phone</div>
    <div class="abs field" style="top:129px;height:30px;line-height:16px">Message</div>
    <div class="abs submit">SUBMIT</div>
  </form>
</footer>

<div class="abs bottombar">© 2016 Veltaro All rights reserved</div>
</body>
</html>
```